Recruitment of Luzon Staffing for the UK market

I want a website for the UK market to attract businesses and companies to come to us for Philipine labour. We want an information site that gives all information on what we do and how we can recruit Philippine labour.
This is a recruitment site for companies to contact us with their requirements for skilled workers coming from the Philipines over to the UK to work.

Target Market(s)

Uk Companies and businesses who want Philipine skilled workers

Industry/Entity Type

REcruitment

Coding

Coded - Design and coding required

Number of Pages Required

5+ page

Font styles to use
Sans Serif

Colors
0054AA
0677BA
7BADD7
CADEEF
E8F1F8
0094D4
00A9DD
6FCCEA
C7EBF8
E9F6FB
EE7325
F08F49
F5BC92
FAE3D3
FDF4ED
EB3D1F
EC4F4E
F09395
F8D3D4
FCEDEE

Requirements
Must have
• Look professional and corperate with drop down menus for Home ,about, services,articles. training , contact us
Nice to have
• Look at Tovel recruitment- https://tovelrecruitment.example.co.uk/. This is my current site - https://www.brindlestaffing.example.com/
Should not have
• Cartoons or silly pictures , needs to be corperate looking

```html
<!DOCTYPE html>
<html lang="en">
<head>
<meta charset="utf-8">
<title>Luzon Staffing – Skilled Philippine Workers for UK Companies</title>
<link rel="stylesheet" href="https://fonts.googleapis.com/css2?family=Poppins:wght@400;500;600;700;800&display=swap">
<style>
:root{
  --red:#9c2b27;
  --red-deep:#86221f;
  --pink:#f9e2e1;
  --ink:#1d1b1b;
  --text:#3d3d3d;
  --muted:#8a8a8a;
  --line:#d9d2d2;
  --night:#1f1b1b;
  --white:#ffffff;
}
*{box-sizing:border-box;margin:0;padding:0}
html,body{width:1200px;height:5324px;overflow:hidden}
body{position:relative;background:var(--white);font-family:'Poppins',sans-serif;color:var(--ink)}
.abs{position:absolute}
a{color:inherit;text-decoration:none}

/* header */
.brand{display:flex;align-items:center;gap:8px;font-weight:700;font-size:20px;color:var(--red);letter-spacing:-.2px}
.brand-mark{width:16px;height:16px;background:var(--red)}
.main-nav{top:32px;right:85px;display:flex;gap:38px;font-size:10px;font-weight:500;letter-spacing:.4px;color:var(--ink)}

/* hero */
.hero-title{left:170px;top:142px;width:860px;font-size:44px;line-height:54px;font-weight:700;color:var(--ink)}
.hero-title .accent{color:var(--red);font-weight:800}
.hero-title .indent{display:block;padding-left:257px}
.hero-copy{left:170px;top:346px;width:440px;font-size:11px;line-height:23.5px;color:var(--text)}
.hero-link{left:170px;top:522px;font-size:12.5px;font-weight:500;color:var(--red)}
.badge{left:772px;top:334px;width:116px;height:116px}
.stats{left:620px;top:512px;display:flex;gap:34px;align-items:center}
.stat{display:flex;align-items:center;gap:8px}
.stat b{font-size:25px;font-weight:700}
.stat span{font-size:8.5px;line-height:10px;color:var(--muted)}

/* about band */
.pink-band{left:0;top:1001px;width:1200px;height:692px;background:var(--pink)}
.about-shape{left:0;top:646px}
.worker-photo{left:842px;top:578px;width:278px;height:423px;border-radius:120px 120px 0 0;background:linear-gradient(180deg,#f1f1f1 0%,#e9d47a 38%,#e6b92f 55%,#2f4f8e 100%)}
.about-title{left:170px;top:690px;font-size:37px;font-weight:700}
.about-title span{color:var(--red)}
.about-sub{left:170px;top:750px;font-size:14px;color:var(--red);font-weight:500}
.about-copy{left:170px;top:806px;width:440px;font-size:11px;line-height:22.5px;color:var(--text)}
.btn-outline{display:flex;align-items:center;justify-content:center;border:1.5px solid var(--red);border-radius:30px;font-size:10px;font-weight:500;color:var(--red);letter-spacing:.3px}
.btn-learn{left:170px;top:944px;width:162px;height:42px}

.service{top:1086px;width:203px;height:256px;background:var(--red);padding:38px 28px 0 28px;color:var(--white)}
.service-icon{width:40px;height:40px;border:2px solid rgba(255,255,255,.85);border-radius:8px}
.service h3{margin-top:42px;font-size:14px;font-weight:600}
.service .go{position:absolute;left:28px;bottom:26px;width:24px;height:24px;border-radius:50%;background:var(--white);display:flex;align-items:center;justify-content:center}
.btn-more{left:522px;top:1388px;width:155px;height:42px}
.back-top{left:40px;top:1490px;width:52px;height:100px}
.back-top span{position:absolute;left:0;top:78px;transform:rotate(-90deg);transform-origin:left top;font-size:10px;color:var(--text);white-space:nowrap}
.back-top i{position:absolute;left:26px;top:0;width:1px;height:28px;background:var(--ink)}

.video{left:162px;top:1498px;width:876px;height:450px;background:var(--white);border-radius:8px;box-shadow:0 6px 24px rgba(0,0,0,.12);padding:8px}
.video-fill{width:100%;height:100%;border-radius:6px;background:linear-gradient(135deg,#c9ccd2 0%,#8e97a4 40%,#5f6b7a 70%,#a7aeb8 100%);position:relative}
.play{position:absolute;left:50%;top:50%;width:62px;height:62px;margin:-31px 0 0 -31px;border-radius:50%;background:var(--white);display:flex;align-items:center;justify-content:center}

/* working together */
.eyebrow{left:0;top:2020px;width:1200px;text-align:center;font-size:12.5px;letter-spacing:4px;color:var(--ink);font-weight:500}
.team-title{left:0;top:2046px;width:1200px;text-align:center;font-size:36px;line-height:46px;font-weight:700}
.team-title span{color:var(--red)}
.info-card{width:408px;height:283px;background:var(--white);border-top:3px solid var(--red);box-shadow:0 4px 20px rgba(0,0,0,.09);padding:36px 28px 0 28px}
.info-card h4{font-size:14.5px;font-weight:600}
.info-card .rule{margin:26px 0 26px;height:1px;background:#e6e0e0}
.info-card p{font-size:10.3px;line-height:20.6px;color:var(--text)}
.info-card .ico{position:absolute;right:36px;top:24px;width:58px;height:52px;border:2px solid #2b2b2b;border-radius:6px}
.info-card .ico::after{content:"";position:absolute;right:-6px;bottom:-6px;width:20px;height:16px;background:var(--red);border-radius:3px}

/* map */
.map{left:0;top:2740px;width:1200px;height:543px;background:linear-gradient(180deg,#ffffff 0%,#e4ecfb 30%,#a9c2f1 62%,#6f95e4 100%)}
.map-title{left:0;top:2836px;width:1200px;text-align:center;font-size:26px;line-height:34px;font-weight:700}
.map-title span{color:var(--red)}

/* people */
.people-title{left:166px;top:3380px;font-size:29px;line-height:36px;font-weight:700}
.people-title span{color:var(--red)}
.read-more{font-size:11px;font-weight:500;color:var(--red)}
.person{top:3362px;height:314px}
.person-label{top:3694px;font-size:15px;font-weight:500}

/* accordion */
.acc-line{left:170px;width:590px;height:1px;background:var(--line)}
.acc-toggle{left:695px;width:30px;height:30px;border-radius:50%;background:var(--red);color:var(--white);display:flex;align-items:center;justify-content:center;font-size:20px;font-weight:500;line-height:1}
.acc-title{left:170px;font-size:17px;font-weight:500}
.acc-body{left:423px;width:330px;font-size:10.3px;line-height:20.6px;color:var(--text)}
.acc-body p+p{margin-top:20px}
.acc-body .link{color:#2c5fc8}
.blog-title{left:820px;top:3820px;font-size:36px;line-height:44px;font-weight:700}
.blog-title span{color:var(--red)}

/* newsletter + footer */
.footer-bg{left:0;top:4873px;width:1200px;height:451px;background:var(--pink)}
.newsletter{left:132px;top:4828px;width:939px;height:97px;background:var(--night);border-radius:50px}
.newsletter h5{position:absolute;left:56px;top:30px;font-size:26px;font-weight:600;color:var(--white)}
.newsletter .field{position:absolute;left:405px;top:25px;width:362px;height:49px;background:var(--white);border-radius:26px 0 0 26px;font-size:10px;color:#9b9b9b;padding:17px 0 0 24px}
.newsletter .send{position:absolute;left:767px;top:25px;width:140px;height:49px;background:var(--red);border-radius:0 26px 26px 0}
.foot-brand{left:128px;top:5004px}
.foot-copy{left:128px;top:5056px;width:230px;font-size:10.5px;line-height:18px;color:var(--text)}
.socials{left:128px;top:5148px;display:flex;gap:10px}
.socials i{width:25px;height:25px;border:1.5px solid var(--red);border-radius:50%}
.socials i.fill{background:var(--red)}
.foot-h{font-size:13px;font-weight:600}
.foot-links{left:428px;top:5018px}
.foot-links ul{list-style:none;margin-top:18px}
.foot-links li{font-size:10.5px;line-height:25px;color:var(--text)}
.foot-contact{left:564px;top:5018px;width:210px}
.contact-row{display:flex;gap:8px;font-size:10.5px;line-height:16px;color:var(--text);margin-top:14px}
.contact-row svg{flex:none;margin-top:2px}
.form-card{left:785px;top:4987px;width:289px;height:248px;background:var(--white);border-top:3px solid var(--red);box-shadow:0 4px 18px rgba(0,0,0,.08);padding:18px 20px}
.form-card .foot-h{font-size:14px}
.form-grid{display:grid;grid-template-columns:1fr 1fr;gap:9px 11px;margin-top:16px}
.input{height:26px;border:1px solid #ddd;font-size:7.5px;color:#777;padding:6px 8px}
.input.area{grid-column:1 / 3;height:58px}
.form-send{display:block;margin:14px auto 0;width:102px;height:27px;border-radius:16px;background:var(--red);color:var(--white);font-size:8px;font-weight:600;text-align:center;line-height:27px}
.legal{left:0;top:5290px;width:1200px;height:34px;background:#f3d4d3;font-size:9.5px;color:var(--text)}
.legal .l{position:absolute;left:122px;top:11px}
.legal .r{position:absolute;right:128px;top:11px}
</style>
</head>
<body>

<!-- header -->
<div class="abs brand" style="left:70px;top:26px"><i class="brand-mark"></i>Luzon Staffing</div>
<nav class="abs main-nav">
  <a>HOME</a><a>ABOUT US</a><a>SERVICES</a><a>ARTICLES</a><a>TRAINING</a><a>CONTACT US</a>
</nav>

<!-- hero -->
<h1 class="abs hero-title"><span class="accent">RECRUITING AND</span><br><span class="accent">PLACING SKILLED:</span> Philippine workers<span class="indent">into UK companies</span></h1>
<p class="abs hero-copy">The Philippine Recruitment Team will monitor the flight of the candidates until they arrive in the United Kingdom to ensure smooth and hassle-free travel of the candidates. If you have selected our pastoral care a member of our team will be awaiting in arrivals at the designated airport and bring them to the place of employment / accommodation and support them over their first 48 hours in person, followed by a lifetime support.</p>
<a class="abs hero-link">We Couldn't agree more...</a>

<svg class="abs badge" viewBox="0 0 116 116" aria-label="Hire us badge">
  <defs><path id="ring" d="M58,58 m-40,0 a40,40 0 1,1 80,0 a40,40 0 1,1 -80,0"/></defs>
  <circle cx="58" cy="58" r="57" fill="#9c2b27"/>
  <circle cx="58" cy="58" r="28" fill="#fff"/>
  <text font-family="Poppins,sans-serif" font-size="9" font-weight="600" fill="#fff" letter-spacing="1.5"><textPath href="#ring">HIRE US · GET HIRED · HIRE US · GET HIRED ·</textPath></text>
  <path d="M48 68 L68 48 M56 48 H68 V60" stroke="#9c2b27" stroke-width="2.5" fill="none" stroke-linecap="round"/>
</svg>

<div class="abs stats">
  <div class="stat"><b>5500+</b><span>People<br>Recruited</span></div>
  <div class="stat"><b>100+</b><span>Happy<br>Clients</span></div>
  <div class="stat"><b>10+</b><span>Countries</span></div>
</div>

<!-- about -->
<div class="abs pink-band"></div>
<svg class="abs about-shape" width="830" height="356" viewBox="0 0 830 356">
  <polygon points="0,0 560,0 790,356 0,356" fill="#f9e2e1"/>
  <polygon points="566,0 584,0 818,356 800,356" fill="#9c2b27"/>
</svg>
<div class="abs worker-photo" role="img" aria-label="Photo of a smiling engineer in a white hard hat and yellow safety vest, arms crossed"></div>

<h2 class="abs about-title">About <span>Philippines</span></h2>
<p class="abs about-sub">The Human, We Feeling, Innovation</p>
<p class="abs about-copy">We source skilled workers directly from the Philippines to work in the UK. With offices, training locations and specialist recruiters we can find the highest quality individuals to add value and resources to any UK business. We delivery quality based on vast experience over a number of years.</p>
<a class="abs btn-outline btn-learn">LEARN MORE</a>

<div class="abs service" style="left:170px"><div class="service-icon" role="img" aria-label="Engineer icon"></div><h3>Civil Engineer</h3><span class="go"><svg width="10" height="10" viewBox="0 0 10 10"><path d="M3.5 2 L6.5 5 L3.5 8" stroke="#9c2b27" stroke-width="1.8" fill="none"/></svg></span></div>
<div class="abs service" style="left:390px"><div class="service-icon" role="img" aria-label="Globe icon"></div><h3>Geographer</h3><span class="go"><svg width="10" height="10" viewBox="0 0 10 10"><path d="M3.5 2 L6.5 5 L3.5 8" stroke="#9c2b27" stroke-width="1.8" fill="none"/></svg></span></div>
<div class="abs service" style="left:613px"><div class="service-icon" role="img" aria-label="Blueprint icon"></div><h3>Structural Engineer</h3><span class="go"><svg width="10" height="10" viewBox="0 0 10 10"><path d="M3.5 2 L6.5 5 L3.5 8" stroke="#9c2b27" stroke-width="1.8" fill="none"/></svg></span></div>
<div class="abs service" style="left:836px"><div class="service-icon" role="img" aria-label="Scientist icon"></div><h3>Social Scientist</h3><span class="go"><svg width="10" height="10" viewBox="0 0 10 10"><path d="M3.5 2 L6.5 5 L3.5 8" stroke="#9c2b27" stroke-width="1.8" fill="none"/></svg></span></div>

<a class="abs btn-outline btn-more">MORE SERVICES</a>
<div class="abs back-top"><i></i><span>Back to Top</span></div>

<div class="abs video">
  <div class="video-fill" role="img" aria-label="Video still of a recruiter greeting a team of workers in a warehouse">
    <span class="play"><svg width="20" height="22" viewBox="0 0 20 22"><path d="M3 2 L18 11 L3 20 Z" fill="#1d1b1b"/></svg></span>
  </div>
</div>

<!-- working together -->
<p class="abs eyebrow">WORKING TOGETHER</p>
<h2 class="abs team-title">We recruit the finest talent available with<br><span>our dedicated 200 strong team.</span></h2>

<div class="abs info-card" style="left:170px;top:2185px">
  <h4>Civil Engineer</h4><i class="ico" role="img" aria-label="Engineer icon"></i><div class="rule"></div>
  <p>Our company has been established in the Philippines for over 20 years. We have mainly been recruiting philippine workers for the off shore industry in asia but since brexit and the new rules on skilled workers entering the UK we have been working with UK companies who now have chance to recruit some of the finest hard working talent from the Philippines for their companies..</p>
</div>
<div class="abs info-card" style="left:620px;top:2185px">
  <h4>How we help</h4><i class="ico" role="img" aria-label="Checklist icon"></i><div class="rule"></div>
  <p>We work with companies to find skilled workers that meet the UK requirements for Visas and work permits. We guide you through the whole process and deliver highly trained people that add value to your business. We are here to help both the companies and the Philippino people to gain a better standard of living for their families.</p>
</div>
<div class="abs info-card" style="left:170px;top:2505px">
  <h4>Where to start</h4><i class="ico" role="img" aria-label="Recruiter icon"></i><div class="rule"></div>
  <p>We need to know what your issues are and how we can understand the personnal you require , over what time frame and the number of employees you need. Once this is established we start sourcing workers in the Philippines that meet your criteria while starting the process in the UK to be able to have all the documents in place to deliver your company hard working skilled individuals.</p>
</div>
<div class="abs info-card" style="left:620px;top:2505px">
  <h4>Contact us today</h4><i class="ico" role="img" aria-label="Phone icon"></i><div class="rule"></div>
  <p>Please contact us today with your requirements , this can be care workers ,chef, welders, pipe fitters, caravan cabinet makers, medical workers. The UK list of required skills is extensive and the Philippines offersenglish speaking highly qualified hard working employees. Contact us today and make that first step to a highly motivated , quality skilled workforce.</p>
</div>

<!-- map -->
<div class="abs map" role="img" aria-label="Map of the Philippines with our recruitment centres marked in red"></div>
<h2 class="abs map-title">Our centres are highlighted in<br><span>Red Dots on the map.</span></h2>

<!-- people -->
<h2 class="abs people-title">We help you find<br>the right <span>People for</span><br><span>your Business</span></h2>
<a class="abs read-more" style="left:166px;top:3529px">Read More ↗</a>
<div class="abs person" style="left:496px;width:279px;background:linear-gradient(180deg,#e9eef2 0%,#dfe3e6 45%,#e6c33a 75%,#8f9398 100%)" role="img" aria-label="Photo of a civil engineer in a hard hat working at a laptop"></div>
<div class="abs person" style="left:791px;width:279px;background:linear-gradient(180deg,#eef0f2 0%,#c9ced6 40%,#2f6aa8 80%,#3b7bbf 100%)" role="img" aria-label="Photo of a psychiatric nurse in blue scrubs holding a tablet"></div>
<div class="abs person" style="left:1088px;width:112px;background:linear-gradient(180deg,#f0f0f0 0%,#cfd4da 50%,#8e969f 100%)" role="img" aria-label="Photo of a technical director at a computer"></div>
<p class="abs person-label" style="left:496px">Civil Engineer</p>
<p class="abs person-label" style="left:791px">Psychiatric Nurse</p>
<p class="abs person-label" style="left:1088px;white-space:nowrap">Technical director</p>

<!-- accordion -->
<div class="abs acc-line" style="top:3810px"></div>
<span class="abs acc-toggle" style="top:3795px">+</span>
<h3 class="abs acc-title" style="top:3836px">UK Skilled Workers List</h3>
<a class="abs read-more" style="left:170px;top:3895px">Read More ↗</a>
<div class="abs acc-body" style="top:3836px"><p>The UK government since brexit have developed a new system based on points (similar to Australia) when recruiting from outside of the UK. Previuosly EU citizens could work in the UK without any extensive documentation or clarification of skills. This has all changed. Overseas recruitment must now focus on skills that are currently short in the UK. The list is extensive and is constandly being reviewed.</p></div>

<div class="abs acc-line" style="top:4016px"></div>
<span class="abs acc-toggle" style="top:4001px">−</span>
<h3 class="abs acc-title" style="top:4053px">Sponsor Licence</h3>
<a class="abs read-more" style="left:170px;top:4112px">Read More ↗</a>
<div class="abs acc-body" style="top:4053px">
  <p>If you have areas of your business that meet the entry requirements of skilled labour your next step is to gain a sponsor licence for your business. There are different types of licences depending on the size of the business.<br>All information can be found here-</p>
  <p class="link">https://www.sponsor-licence.example.org/apply</p>
  <p>It si estimated that the whole process takes between 20 and 30 minutes and approximatly 6 weeks thereafter to be approved.</p>
  <p>The documentation required are as follows.</p>
  <p>Copy of your standard terms of employment. Addendum to Contract. Client Manpower Request Visa Guarantee Letter Letter of Undertaking CAS Service Agreement Business certificate of registration if limited company, or letter from Accountants, if business is a sole proprietorship or a partnership, as proof of business Passport copy of the signatory.</p>
  <p>We can help with all this once you have made contact and have an idea of your needs.</p>
</div>

<div class="abs acc-line" style="top:4570px"></div>
<span class="abs acc-toggle" style="top:4555px">+</span>
<h3 class="abs acc-title" style="top:4611px">Recruitment Timeline</h3>
<a class="abs read-more" style="left:170px;top:4670px">Read More ↗</a>
<div class="abs acc-body" style="top:4611px">
  <p>Brief us on the job profiles – this is passed on to our teams in the Philippines.</p>
  <p>• Our teams in the Philippines source suitable candidates, documentation required for each candidate will be checked and vetted by the Recruitment Team. Once deemed qualified, they will now be assessed by their Technical Interviewer .</p>
</div>

<h2 class="abs blog-title">Read our<br>recent <span>Blog</span><br><span>Articles</span></h2>
<a class="abs read-more" style="left:822px;top:3974px">See all articles ↗</a>

<!-- newsletter + footer -->
<div class="abs footer-bg"></div>
<div class="abs newsletter">
  <h5>Subscribe Newsletter</h5>
  <div class="field">Enter Your Email</div>
  <div class="send"></div>
</div>

<div class="abs brand foot-brand"><i class="brand-mark"></i>Luzon Staffing</div>
<p class="abs foot-copy">We source skilled workers directly from the Philippines to work in the UK. With offices , training locations and specialist...</p>
<div class="abs socials"><i></i><i class="fill"></i><i></i><i></i></div>

<div class="abs foot-links">
  <h6 class="foot-h">Quick Links</h6>
  <ul><li>Home</li><li>About</li><li>Services</li><li>Articles</li><li>Training</li><li>Contact Us</li></ul>
</div>

<div class="abs foot-contact">
  <h6 class="foot-h">Contact Details</h6>
  <div class="contact-row" style="margin-top:18px"><svg width="11" height="13" viewBox="0 0 11 13"><path d="M5.5 0.5a4.5 4.5 0 0 1 4.5 4.5c0 3.3-4.5 7.5-4.5 7.5S1 8.3 1 5a4.5 4.5 0 0 1 4.5-4.5z" fill="#9c2b27"/><circle cx="5.5" cy="5" r="1.6" fill="#fff"/></svg><span>Orchard Court,<br>Eastholme EH4 2ZZ,<br>United Kingdom</span></div>
  <div class="contact-row"><svg width="12" height="12" viewBox="0 0 12 12"><path d="M2.5 1l2 2.5-1.2 1.3a7 7 0 0 0 3.9 3.9L8.5 7.5 11 9.5 9.8 11C5 11 1 7 1 2.2z" fill="#9c2b27"/></svg><span>07700 900418</span></div>
  <div class="contact-row"><svg width="13" height="10" viewBox="0 0 13 10"><rect x="0.5" y="0.5" width="12" height="9" fill="#9c2b27"/><path d="M1 1l5.5 4.5L12 1" stroke="#fff" fill="none"/></svg><span>hello@luzonstaffing.example.com</span></div>
</div>

<div class="abs form-card">
  <h6 class="foot-h">Contact Us Today</h6>
  <div class="form-grid">
    <div class="input">First Name</div><div class="input">Last Name</div>
    <div class="input">Phone Number</div><div class="input">Email Address</div>
    <div class="input area">Message</div>
  </div>
  <a class="form-send">Send Message</a>
</div>

<div class="abs legal"><span class="l">Copyrights © 2023 All Rights Reserved | Luzon Staffing Ltd</span><span class="r">Privacy Policy &nbsp; | &nbsp; Terms of Use</span></div>

</body>
</html>
```